Wedding and event Photography company.

We need a business card design for a photography company based in Singapore named TamKeza. Our core service offering is wedding photojournalism. We would like to see minimalistic designs that use the colour white. The final design should communicate a sense of ease and reliability.

The attached are a couple of visual reference which i found over the web, i hope it will helps.

Project Brief Update (14th July 2014):
- Please refrain from using any images from the website for the design. The laws and regulations over here does not allow me to distribute my client's images. Thanks!

Target Market(s)

Young and middle aged adults aged 24 - 38. With money to spend =D

Industry/Entity Type

Business

Contact Information for Business Card

Name: Dev Lunor
Designation: Head Photographer
Mobile: +65 81749026
Email: jun@tamkeza.example
Website: www.tamkeza.example

Font styles to use
Other font styles liked:
• Baskerville URW

Colors

Designer to choose colors to be used in the design.

Requirements
Must have
• Must include:
• - The brand TamKeza
• - The logo attached
• - Please help to place the brand TamKeza with the logo according to your preferences.
• - Services
• - Wedding Photography
• - Portraiture
• - Photojournalism
Nice to have
• Looking forward to an elegant and simple design. Please see attached examples!
• Please use Serif Fonts
Should not have
• Please refrain from using dark tones for the majority of the design.
• Please refrain from letterpress and embossing.

```html
<!DOCTYPE html>
<html lang="en">
<head>
<meta charset="utf-8">
<title>TamKeza Business Card</title>
<link href="https://fonts.googleapis.com/css2?family=Libre+Baskerville:wght@400;700&display=swap" rel="stylesheet">
<style>
  :root {
    --backdrop: #3a3a3a;
    --card: #ffffff;
    --ink: #111111;
    --ink-soft: #444444;
    --frame-light: #c4c4c4;
    --frame-dark: #111111;
  }
  * { margin: 0; padding: 0; box-sizing: border-box; }
  html, body {
    width: 1200px; height: 801px; overflow: hidden;
    background: var(--backdrop);
    font-family: "Libre Baskerville", Georgia, serif;
    color: var(--ink);
  }
  .card {
    position: absolute;
    top: 246px;
    width: 540px; height: 309px;
    background: var(--card);
  }
  .card--front { left: 40px; }
  .card--back { left: 620px; }

  .frame {
    position: absolute; inset: 14px;
    border: 5px solid var(--frame-light);
  }
  .card--back .frame { border-color: var(--frame-dark); inset: 16px; }

  .contact {
    position: absolute; left: 42px; top: 44px;
    font-variant: small-caps;
  }
  .contact__name { font-size: 22px; letter-spacing: 0.5px; line-height: 1; }
  .contact__role { font-size: 14px; color: var(--ink-soft); margin-top: 4px; }
  .contact__list { list-style: none; margin-top: 16px; }
  .contact__item {
    display: flex; align-items: center; gap: 8px;
    font-size: 13px; line-height: 1; margin-bottom: 7px;
    font-variant: normal; text-transform: uppercase; letter-spacing: 0.3px;
  }
  .contact__icon { width: 16px; height: 16px; flex: none; }

  .services { margin-top: 22px; }
  .services__title { font-size: 16px; font-weight: 700; line-height: 1.1; }
  .services__list { list-style: none; font-size: 13px; line-height: 1.3; color: var(--ink-soft); }

  .brand-name {
    position: absolute;
    font-size: 46px; font-weight: 400; color: var(--ink);
    line-height: 1;
  }
  .card--front .brand-name { right: 46px; top: 100px; }
  .card--back .brand-name { left: 0; right: 0; top: 108px; text-align: center; font-size: 54px; }

  .website {
    position: absolute;
    font-size: 13px; letter-spacing: 0.5px;
    text-transform: uppercase;
  }
  .card--front .website { right: 42px; bottom: 38px; }
  .card--back .website { left: 0; right: 0; bottom: 58px; text-align: center; }
</style>
</head>
<body>

<section class="card card--front">
  <div class="frame"></div>
  <div class="contact">
    <p class="contact__name">Dev Lunor</p>
    <p class="contact__role">Head Photographer</p>
    <ul class="contact__list">
      <li class="contact__item">
        <svg class="contact__icon" viewBox="0 0 16 16" aria-hidden="true">
          <circle cx="8" cy="8" r="8" fill="#111"/>
          <rect x="5.5" y="3.5" width="5" height="9" rx="1" fill="#fff"/>
          <rect x="6.3" y="4.6" width="3.4" height="5.6" fill="#111"/>
        </svg>
        +65 81749026
      </li>
      <li class="contact__item">
        <svg class="contact__icon" viewBox="0 0 16 16" aria-hidden="true">
          <circle cx="8" cy="8" r="8" fill="#111"/>
          <rect x="3.8" y="5" width="8.4" height="6" fill="#fff"/>
          <path d="M3.8 5 L8 8.4 L12.2 5" fill="none" stroke="#111" stroke-width="0.9"/>
        </svg>
        jun@tamkeza.example
      </li>
    </ul>
    <div class="services">
      <p class="services__title">Services</p>
      <ul class="services__list">
        <li>Wedding Photography</li>
        <li>Portraiture</li>
        <li>Photojournalism</li>
      </ul>
    </div>
  </div>
  <p class="brand-name">TamKeza</p>
  <p class="website">www.tamkeza.example</p>
</section>

<section class="card card--back">
  <div class="frame"></div>
  <p class="brand-name">TamKeza</p>
  <p class="website">www.tamkeza.example</p>
</section>

</body>
</html>
```